Animal Horse & Bedding Company Needs a Website Coded & Designed

We need a website for a new animal bedding and feed company that is visually grabbing and vibrant. We would like to see a website that displays trust, quality and confidence. Needs to be responsive and mobile friendly for all browsers and coded for both Android & IOS. SEO is also important.

Joomla or Wordpress – must be both desktop and mobile friendly with fast page load speed. Need the ability to edit ourselves in Wordpress or Joomla.

Full details attached below with some layout and content ideas.

Coding

Coded - Design and coding required

Number of Pages Required

5+ page

Font styles to use
Sans Serif

Requirements
Must have
• Needs to be responsive and mobile friendly for all browsers and coded for both Android & IOS. SEO is also important.

Wordpress – must be both desktop and mobile friendly with fast page load speed. Need the ability to edit ourselves in Wordpress.

Logo Colours:
Dark Brown
CMYK: 50 / 70 / 80 / 70
Pantone: 4625C

Orange
CMYK: 0 / 50 / 100 / 0
Pantone: 144C
Nice to have
• Use picture of building attached and super impose logo on building.

```html
<!DOCTYPE html>
<html lang="en">
<head>
<meta charset="utf-8">
<title>Golden Furrow – Bedding &amp; Feed</title>
<link rel="stylesheet" href="https://fonts.googleapis.com/css2?family=Oswald:wght@400;500;600&family=Lato:wght@400;700&family=Montserrat:wght@600;700&display=swap">
<style>
:root{
  --brown:#3d2314;
  --brown-deep:#2f1a0e;
  --orange:#f7941d;
  --orange-soft:#f5a43a;
  --grey-band:#e1e1e1;
  --text:#5a5a5a;
  --white:#ffffff;
}
*{margin:0;padding:0;box-sizing:border-box}
html,body{width:1200px;height:3026px;overflow:hidden}
body{position:relative;font-family:"Lato",sans-serif;color:var(--text);background:var(--white)}
.abs{position:absolute}
.brand{display:flex;align-items:center;gap:10px;font-family:"Oswald",sans-serif;font-weight:500;color:var(--brown);letter-spacing:3px;text-transform:uppercase}
.brand-dot{border-radius:50%;border:4px solid var(--orange);flex:none}
/* top bar */
.topbar{top:0;left:0;width:1200px;height:24px;background:var(--brown);color:#fff;font:700 11px "Lato",sans-serif;display:flex;align-items:center;justify-content:space-between;padding:0 110px 0 122px}
.topbar .phone{color:var(--orange)}
.topbar .follow{display:flex;align-items:center;gap:4px}
.soc{display:inline-block;width:12px;height:12px;border-radius:50%;background:var(--orange)}
/* hero */
.hero{top:24px;left:0;width:1200px;height:693px;background:linear-gradient(180deg,#cfd8dc 0%,#b7c3a6 28%,#7f8a4d 45%,#6f6a32 65%,#8a6e35 100%)}
.hero-horse{left:650px;top:170px;width:560px;height:540px;background:radial-gradient(ellipse at 45% 45%,#9a4a1c 0%,#7a3512 45%,rgba(120,70,30,0) 72%)}
.nav{top:60px;display:flex;gap:52px;font:500 19px "Oswald",sans-serif;color:var(--brown);text-transform:uppercase}
.nav-left{left:102px}
.nav-right{left:768px;gap:44px;top:54px}
.header-brand{left:420px;top:44px;font-size:32px}
.header-brand .brand-dot{width:44px;height:44px}
.btn-quote-top{left:970px;top:49px;width:128px;height:32px;border-radius:16px;background:var(--brown);color:var(--orange);font:500 15px "Oswald",sans-serif;display:flex;align-items:center;justify-content:center}
.hero-title{left:90px;top:352px;font:600 44px/44px "Oswald",sans-serif;color:var(--orange);text-transform:uppercase;letter-spacing:.5px}
.hero-btn{top:531px;height:36px;border-radius:18px;font:500 14px "Oswald",sans-serif;display:flex;align-items:center;justify-content:center;text-transform:uppercase}
.hero-btn.solid{left:88px;width:127px;background:var(--orange);color:var(--brown)}
.hero-btn.ghost{left:246px;width:125px;border:2px solid var(--orange);color:#fff}
/* welcome */
.welcome-brand{left:117px;top:792px}
.welcome-brand .brand-dot{width:54px;height:54px}
.welcome-brand .small{font:500 15px "Oswald",sans-serif;letter-spacing:0;display:block;margin-bottom:-4px}
.welcome-brand .big{font-size:38px;letter-spacing:4px;line-height:1}
.intro{left:117px;top:890px;width:420px;font-size:12px;line-height:16px;text-align:justify}
.intro p{margin-bottom:16px}
.photo{background:#999}
.photo-paddock{left:577px;top:815px;width:456px;height:250px;background:linear-gradient(180deg,#3e5a2a 0%,#4d7a2c 35%,#7db33c 60%,#8cc441 100%)}
.features{top:1098px;left:117px;width:920px;display:flex;align-items:flex-start}
.feature{display:flex;gap:9px;width:290px}
.feature-icon{width:36px;height:36px;border-radius:50%;background:var(--orange);border:3px solid #ffd08a;flex:none;display:flex;align-items:center;justify-content:center}
.feature h4{font:700 13px "Montserrat",sans-serif;color:var(--brown);text-transform:uppercase;margin-top:2px}
.feature p{font-size:9.5px;line-height:12px;color:var(--brown)}
.divider{width:2px;height:56px;background:var(--brown);margin:-6px 34px 0 0;opacity:.6}
/* bedding & feeding */
.band-grey{top:1241px;left:0;width:1200px;height:660px;background:var(--grey-band)}
.photo-straw{left:113px;top:1323px;width:478px;height:488px;background:linear-gradient(160deg,#6a3a18 0%,#b8742f 35%,#d9a445 60%,#c48a2e 100%);box-shadow:0 3px 8px rgba(0,0,0,.25)}
.photo-hay{left:607px;top:1986px;width:476px;height:487px;background:linear-gradient(120deg,#b9b7b1 0%,#8c8882 40%,#a67a34 70%,#3a2a18 100%);box-shadow:0 3px 8px rgba(0,0,0,.25)}
.sec-head{display:flex;align-items:center;gap:12px;font:600 40px "Oswald",sans-serif;color:var(--brown);text-transform:uppercase;letter-spacing:1px}
.sec-head .brand-dot{width:48px;height:48px}
.sec-rule{height:3px;width:52px;background:var(--brown)}
.sec-copy{width:390px;font-size:15px;line-height:16px;text-align:justify;color:#666}
.ticks{list-style:none;font-size:15px;color:#666}
.ticks li{display:flex;align-items:center;gap:16px;height:24px}
.ticks svg{flex:none}
.read-more{height:26px;border-radius:13px;background:var(--brown);color:var(--orange);font:700 9px "Montserrat",sans-serif;letter-spacing:1px;display:flex;align-items:center;gap:10px;padding:0 14px 0 4px}
.read-more span.dot{width:18px;height:18px;border-radius:50%;border:2px solid var(--orange)}
/* newsletter */
.newsletter{top:2552px;left:0;width:1200px;height:203px;background:linear-gradient(180deg,#9fb4c8 0%,#dfe7ee 45%,#c9cdc0 78%,#6f7e3b 100%)}
.news-horses{left:10px;top:2590px;width:260px;height:160px;background:radial-gradient(ellipse at 50% 50%,#8a3e16 0%,#6a2e10 45%,rgba(120,80,40,0) 72%)}
.news-title{left:322px;top:2602px;display:flex;align-items:center;gap:12px;font:600 34px "Oswald",sans-serif;color:var(--brown-deep);letter-spacing:1px;text-transform:uppercase}
.news-title i{width:3px;height:40px;background:var(--brown-deep)}
.news-form{left:315px;top:2658px;width:836px;height:50px;display:flex;border:1px solid var(--brown)}
.news-form .field{flex:1;background:#fff;font-size:13px;color:#333;display:flex;align-items:center;padding-left:40px}
.news-form .go{width:127px;background:var(--brown-deep);color:#fff;font:700 14px "Montserrat",sans-serif;display:flex;align-items:center;justify-content:center}
/* footer */
.footer{top:2755px;left:0;width:1200px;height:229px;background:var(--brown)}
.foot-brand{left:130px;top:2800px;flex-direction:column;gap:6px;color:#fff;font-size:38px;letter-spacing:4px}
.foot-brand .brand-dot{width:52px;height:52px}
.foot-col h5{font:400 14px "Oswald",sans-serif;color:var(--orange);text-decoration:underline;text-transform:uppercase;margin-bottom:12px}
.foot-col ul{list-style:none;font-size:11px;color:#fff}
.foot-col li{display:flex;align-items:center;gap:10px;height:18.5px}
.arrow{width:0;height:0;border-left:6px solid var(--orange);border-top:4px solid transparent;border-bottom:4px solid transparent}
.foot-contact li{align-items:flex-start;height:auto;margin-bottom:4px;line-height:14px}
.foot-contact svg{flex:none;margin-top:2px}
.foot-mail{width:162px;height:26px;display:flex}
.foot-mail .f{flex:1;background:#fff;font-size:8px;color:#888;display:flex;align-items:center;padding-left:12px}
.foot-mail .b{width:28px;background:var(--orange);display:flex;align-items:center;justify-content:center;border-radius:0 4px 4px 0}
.foot-soc{display:flex;gap:3px}
.foot-soc .soc{width:17px;height:17px;background:#fff}
.bottombar{top:2984px;left:0;width:1200px;height:42px;background:var(--orange);color:var(--brown);font-size:13px;display:flex;align-items:center;justify-content:space-between;padding:0 126px 0 127px}
</style>
</head>
<body>

<div class="abs topbar"><span>Call Us : <span class="phone">+1 555 014 2280</span></span><span class="follow">Follow Us: <i class="soc"></i><i class="soc"></i><i class="soc"></i><i class="soc"></i><i class="soc"></i></span></div>

<section class="abs hero" role="img" aria-label="Bay horse standing in a sunlit grassy meadow"></section>
<div class="abs hero-horse" role="img" aria-label="Bay horse"></div>
<nav class="abs nav nav-left"><span>Home</span><span>About</span><span>Feed</span></nav>
<div class="abs brand header-brand"><span class="brand-dot"></span>Golden Furrow</div>
<nav class="abs nav nav-right"><span>Bedding</span><span>Contact Us</span></nav>
<div class="abs btn-quote-top">REQUEST QOUTE</div>
<h1 class="abs hero-title">The best bedding &amp; feed<br>for your horse livestock<br>or household pet</h1>
<div class="abs hero-btn solid">Contact Us</div>
<div class="abs hero-btn ghost">Request Quote</div>

<div class="abs brand welcome-brand"><span class="brand-dot"></span><span><span class="small">WELCOME TO</span><span class="big">Golden Furrow</span></span></div>
<div class="abs intro">
  <p>Looking for the best bedding and feed for your horse, livestock or household pet look no further. We use premium locally sourced straw and hay in all of our products and are committed in providing quality products and service.</p>
  <p>Your animal deserves the very best in health and comfort to keep them healthy, strong and happy. Our products are designed for horses, livestock (goats, cattle and sheep), small caged animals (rabbits, guinea pigs and more).</p>
  <p>Golden Furrow offers supply and delivery of fresh bedding as well as removal of waste bedding. Let us deliver you a container of fresh straw and haul your waste bedding away. A full service solution that is sustainable and responsible.</p>
</div>
<div class="abs photo-paddock" role="img" aria-label="Three horses grazing in a fenced green paddock"></div>

<div class="abs features">
  <div class="feature"><span class="feature-icon"></span><div><h4>Quality Guaranteed</h4><p>Grown for quality - 100% natural with no<br>chemicals or additives</p></div></div>
  <span class="divider"></span>
  <div class="feature"><span class="feature-icon"></span><div><h4>Full Service Solution</h4><p>Dedicated in providing a full service solution<br>of bedding supply &amp; waste removal</p></div></div>
  <span class="divider"></span>
  <div class="feature" style="width:270px"><span class="feature-icon"></span><div><h4>Convenient &amp; Cost Effective</h4><p>Compressed bags, pellets or bulk products saving<br>in shipping costs</p></div></div>
</div>

<section class="abs band-grey"></section>
<div class="abs photo-straw" role="img" aria-label="Mare and foal resting on golden straw bedding"></div>
<div class="abs sec-head" style="left:654px;top:1325px"><span class="brand-dot"></span>Bedding</div>
<div class="abs sec-rule" style="left:660px;top:1405px"></div>
<p class="abs sec-copy" style="left:660px;top:1452px">Hay cubes and pellets are made from premium hay offering a variety of animals a feed that is non-GMO and packed with natural nutrients. These pellets and cubes are less bulky to handle, store and ship.As well, they reduce the amount of wasted feed.</p>
<ul class="abs ticks" style="left:660px;top:1568px">
  <li><svg width="12" height="12" viewBox="0 0 12 12"><circle cx="6" cy="6" r="6" fill="#3d2314"/><path d="M3 6.2l2 2 4-4" stroke="#fff" stroke-width="1.6" fill="none"/></svg>100% Natural Chopped Straw</li>
  <li><svg width="12" height="12" viewBox="0 0 12 12"><circle cx="6" cy="6" r="6" fill="#3d2314"/><path d="M3 6.2l2 2 4-4" stroke="#fff" stroke-width="1.6" fill="none"/></svg>Low Dust</li>
  <li><svg width="12" height="12" viewBox="0 0 12 12"><circle cx="6" cy="6" r="6" fill="#3d2314"/><path d="M3 6.2l2 2 4-4" stroke="#fff" stroke-width="1.6" fill="none"/></svg>Chemical &amp; Additive Free</li>
  <li><svg width="12" height="12" viewBox="0 0 12 12"><circle cx="6" cy="6" r="6" fill="#3d2314"/><path d="M3 6.2l2 2 4-4" stroke="#fff" stroke-width="1.6" fill="none"/></svg>Clean &amp; Highly Absorbent</li>
  <li><svg width="12" height="12" viewBox="0 0 12 12"><circle cx="6" cy="6" r="6" fill="#3d2314"/><path d="M3 6.2l2 2 4-4" stroke="#fff" stroke-width="1.6" fill="none"/></svg>Cheaper than Wood Shavings</li>
  <li><svg width="12" height="12" viewBox="0 0 12 12"><circle cx="6" cy="6" r="6" fill="#3d2314"/><path d="M3 6.2l2 2 4-4" stroke="#fff" stroke-width="1.6" fill="none"/></svg>Economic – less used &amp; less wasted</li>
  <li><svg width="12" height="12" viewBox="0 0 12 12"><circle cx="6" cy="6" r="6" fill="#3d2314"/><path d="M3 6.2l2 2 4-4" stroke="#fff" stroke-width="1.6" fill="none"/></svg>Environmentally Friendly – Recyclable &amp; Compostable</li>
</ul>
<div class="abs read-more" style="left:660px;top:1765px"><span class="dot"></span>READ MORE</div>

<div class="abs sec-head" style="left:106px;top:1992px"><span class="brand-dot"></span>Feeding</div>
<p class="abs sec-copy" style="left:115px;top:2080px">Hay cubes and pellets are made from premium hay offering a variety of animals a feed that is non-GMO and packed with natural nutrients. These pellets and cubes are less bulky to handle, store and ship.As well, they reduce the amount of wasted feed.</p>
<ul class="abs ticks" style="left:112px;top:2191px">
  <li><svg width="12" height="12" viewBox="0 0 12 12"><circle cx="6" cy="6" r="6" fill="#3d2314"/><path d="M3 6.2l2 2 4-4" stroke="#fff" stroke-width="1.6" fill="none"/></svg>100% Natural</li>
  <li><svg width="12" height="12" viewBox="0 0 12 12"><circle cx="6" cy="6" r="6" fill="#3d2314"/><path d="M3 6.2l2 2 4-4" stroke="#fff" stroke-width="1.6" fill="none"/></svg>Chemical &amp; Additive Free</li>
  <li><svg width="12" height="12" viewBox="0 0 12 12"><circle cx="6" cy="6" r="6" fill="#3d2314"/><path d="M3 6.2l2 2 4-4" stroke="#fff" stroke-width="1.6" fill="none"/></svg>Available in Pellets or Cubes</li>
  <li><svg width="12" height="12" viewBox="0 0 12 12"><circle cx="6" cy="6" r="6" fill="#3d2314"/><path d="M3 6.2l2 2 4-4" stroke="#fff" stroke-width="1.6" fill="none"/></svg>High Protein Content</li>
  <li><svg width="12" height="12" viewBox="0 0 12 12"><circle cx="6" cy="6" r="6" fill="#3d2314"/><path d="M3 6.2l2 2 4-4" stroke="#fff" stroke-width="1.6" fill="none"/></svg>Eliminate Waste In Feeding</li>
  <li><svg width="12" height="12" viewBox="0 0 12 12"><circle cx="6" cy="6" r="6" fill="#3d2314"/><path d="M3 6.2l2 2 4-4" stroke="#fff" stroke-width="1.6" fill="none"/></svg>Clean - Eliminates Dust From Feeding Baled Hay</li>
  <li><svg width="12" height="12" viewBox="0 0 12 12"><circle cx="6" cy="6" r="6" fill="#3d2314"/><path d="M3 6.2l2 2 4-4" stroke="#fff" stroke-width="1.6" fill="none"/></svg>Cost Effective</li>
</ul>
<div class="abs read-more" style="left:112px;top:2409px"><span class="dot"></span>READ MORE</div>
<div class="abs photo-hay" role="img" aria-label="Close-up of a horse muzzle eating hay"></div>

<section class="abs newsletter" role="img" aria-label="Open pasture under a cloudy sky"></section>
<div class="abs news-horses" role="img" aria-label="Mare and foal walking in a field"></div>
<div class="abs news-title"><i></i>Subscribe to Newsletter</div>
<div class="abs news-form"><span class="field">Enter Your Email</span><span class="go">SUBSCRIBE</span></div>

<footer class="abs footer"></footer>
<div class="abs brand foot-brand"><span class="brand-dot"></span>Golden Furrow</div>
<div class="abs foot-col" style="left:451px;top:2806px"><h5>Quick Links</h5><ul>
  <li><i class="arrow"></i>Home</li><li><i class="arrow"></i>About</li><li><i class="arrow"></i>Feed</li><li><i class="arrow"></i>Bedding</li><li><i class="arrow"></i>Contact Us</li></ul></div>
<div class="abs foot-col foot-contact" style="left:653px;top:2808px"><h5>Contact Us</h5><ul>
  <li><svg width="10" height="12" viewBox="0 0 10 12"><path d="M5 0a4 4 0 0 1 4 4c0 3-4 8-4 8S1 7 1 4a4 4 0 0 1 4-4z" fill="#f7941d"/><circle cx="5" cy="4" r="1.5" fill="#3d2314"/></svg><span>1420 Meadowbank Road<br>Fairhill, Oregon 97001</span></li>
  <li><svg width="10" height="10" viewBox="0 0 10 10"><path d="M2 0l2 2-1 2 3 3 2-1 2 2-2 2C4 10 0 6 0 2z" fill="#f7941d"/></svg>555-010-4477</li>
  <li><svg width="11" height="9" viewBox="0 0 11 9"><rect width="11" height="9" fill="#f7941d"/><path d="M0 0l5.5 5L11 0" stroke="#3d2314" fill="none"/></svg>hello@goldenfurrow.example</li>
  <li><svg width="10" height="10" viewBox="0 0 10 10"><circle cx="5" cy="5" r="5" fill="#8a5a2a"/></svg>goldenfurrow.example</li></ul></div>
<div class="abs foot-col" style="left:913px;top:2806px"><h5>Newsletter</h5>
  <div class="foot-mail"><span class="f">Email Address</span><span class="b"><svg width="8" height="10" viewBox="0 0 8 10"><path d="M0 0l8 5-8 5z" fill="#2f1a0e"/></svg></span></div>
  <h5 style="margin-top:12px">Follow Us</h5>
  <div class="foot-soc"><i class="soc"></i><i class="soc"></i><i class="soc"></i><i class="soc"></i><i class="soc"></i></div>
</div>
<div class="abs bottombar"><span>Copyright © 2021, Northgate Studio, All Right Reserved</span><span>Delivery in Canada &amp; USA</span></div>

</body>
</html>
```